依頼概要
■依頼の目的/概要
薬局で作っているかぜ薬の販促用のポスターを作成して頂きたいです。

■依頼詳細
以下の4つの文言と当社の社長の写真を入れたポスターのデザインをお願いします。

・私が毎日心を込めて作っております(キャッチコピー)
・薬剤師手作りのかぜ薬(キャッチコピーの下に一回り小さい文字でいれる)
・一度飲んだら手放せなくなります
・特に仕事で忙しくて病院に行けない方はご家庭に必携です
・社長の写真

薬局内に掲示するポスターになります。
実際に掲示するポスターのサイズはA0サイズで考えていますが、デザインはA4サイズでの作成をお願いいたします。
※社長の写真は添付ファイルにてご確認ください。

その他何かご不明な点がございましたら、お気軽にご質問下さい。
よろしくお願いいたします。
ポスター内の文字に関して、縦書きなら縦書き、横書きなら横書きに統一をお願いいたします。

仕事で忙しい方にも目にとまるようなデザインだったので、選ばせていただきました。

提案していただいたランサーの皆さん、ありがとうございました。

```html
<!DOCTYPE html>
<html lang="ja">
<head>
<meta charset="UTF-8">
<title>薬剤師手作りのかぜ薬</title>
<link href="https://fonts.googleapis.com/css2?family=Noto+Serif+JP:wght@500;700;900&display=swap" rel="stylesheet">
<style>
  :root {
    --navy: #0d2a6b;
    --blue-deep: #1f4fa8;
    --blue-soft: #cfe0f5;
    --blue-pale: #eef4fb;
    --ink: #1b1b2a;
    --white: #ffffff;
    --photo-skin: #c9a28a;
    --photo-coat: #a9bfdc;
  }
  * { margin: 0; padding: 0; box-sizing: border-box; }
  html, body { width: 846px; height: 1200px; overflow: hidden; }
  body { font-family: "Noto Serif JP", serif; background: var(--white); }

  .poster {
    position: relative;
    width: 846px;
    height: 1200px;
    overflow: hidden;
    background:
      radial-gradient(ellipse at 30% 10%, var(--white) 0%, transparent 55%),
      linear-gradient(180deg, var(--blue-soft) 0%, var(--blue-pale) 30%, var(--white) 50%);
  }

  .portrait {
    position: absolute;
    left: 0; top: 600px;
    width: 846px; height: 600px;
    background:
      linear-gradient(180deg, var(--white) 0%, rgba(255,255,255,0) 25%),
      radial-gradient(ellipse at 45% 55%, var(--photo-skin) 0%, #b89583 28%, transparent 48%),
      linear-gradient(180deg, #d9e2ee 20%, var(--photo-coat) 70%, #8fa9cf 100%);
  }

  .vertical { position: absolute; writing-mode: vertical-rl; white-space: nowrap; }

  .headline {
    font-weight: 900;
    color: var(--white);
    line-height: 1;
    text-shadow:
      0 0 3px var(--navy), 0 0 6px var(--navy), 0 0 10px var(--blue-deep),
      3px 3px 0 var(--navy), -3px -3px 0 var(--navy), 3px -3px 0 var(--navy), -3px 3px 0 var(--navy);
  }
  .headline--first { right: 16px; top: 18px; font-size: 124px; }
  .headline--second { left: 12px; top: 296px; font-size: 124px; }

  .product-label { right: 241px; top: 160px; font-size: 54px; font-weight: 700; color: var(--ink); line-height: 1; }
  .product-name { right: 301px; top: 388px; font-size: 66px; font-weight: 900; color: var(--ink); line-height: 1; }

  .body-copy {
    right: 401px; top: 220px;
    font-size: 31px; font-weight: 500; color: var(--ink);
    line-height: 1.26;
  }
</style>
</head>
<body>
  <main class="poster">
    <div class="portrait" role="img" aria-label="薬局で風邪薬を調合する薬剤師の写真"></div>

    <h1 class="vertical headline headline--first">私が毎日心を込めて</h1>
    <p class="vertical headline headline--second">作っております</p>

    <p class="vertical product-label">薬剤師手作りの</p>
    <h2 class="vertical product-name">かぜ薬</h2>

    <p class="vertical body-copy">一度飲んだら手放せなく<br>なります<br>特に仕事で忙しくて病院に<br>行けない方は<br>ご家庭に必携です</p>
  </main>
</body>
</html>
```